Travel Website Design

My client is a startup that will sell Cedar Reach and fishing trips.
We do not have a logo as of yet, but I have attached 3 options for you to use in the mockup process. Please feel free to use any one (or all 3) of them, but don't base design around them.

Also attached is client's loose idea of how he wants an interior page to look. For the homepage, it would definitely need a rotating image slider, a search, and a tabbed section. The bluecranereelcasting.com is probably closest to what he is looking for.

Here are a few websites to pass along. In addition to the logos I have attached some links of company websites that are competition and have similar designs and layouts similar to what I am looking for.

http://www.bluecranereelcasting.com - The most direct competition that I have. I really like how they layout the pages and lodges info.

Tarvo.com - Close competition. Not a huge fan of how they search for lodges but like how they display each lodge and provide info.

http://www.qirandel.com/ - Example of a company website and layout the client does not like.

http://stonebrookjourneys.com/ - Clean feel. Not a fan of how they layout each lodges info.

```html
<!DOCTYPE html>
<html lang="en">
<head>
<meta charset="utf-8">
<title>Cedar Reach – Fly Fishing &amp; Sport Fishing Trips</title>
<link rel="stylesheet" href="https://fonts.googleapis.com/css2?family=Ubuntu:ital,wght@0,400;0,500;0,700;1,400;1,500&family=Open+Sans:wght@400;600&display=swap">
<style>
:root{
  --ink:#222226;
  --blue:#0d6e9c;
  --blue-band:#0a6fa0;
  --black:#151517;
  --page:#e6e6ec;
  --card:#eeeef4;
  --text:#3a3a3e;
  --footer:#1e1e20;
  --footer-text:#d8d8d8;
  --white:#ffffff;
}
*{box-sizing:border-box;margin:0;padding:0}
html,body{width:1005px;height:1200px;overflow:hidden}
body{position:relative;background:var(--page);font-family:"Open Sans",sans-serif;color:var(--text)}
.abs{position:absolute}

/* header */
.header{left:0;top:0;width:1005px;height:108px;background:var(--white);border-top:6px solid var(--black);border-bottom:6px solid var(--black)}
.brand{left:117px;top:22px;display:flex;align-items:center;gap:14px}
.brand-mark{width:64px;height:64px;background:var(--blue);border-radius:3px}
.brand-name{font-family:"Ubuntu",sans-serif;font-weight:700;font-size:29px;line-height:31px;color:var(--ink)}
.member-tab{left:572px;top:0;width:148px;height:34px;background:var(--black);color:var(--white);font-family:"Ubuntu",sans-serif;font-weight:500;font-size:13px;display:flex;align-items:center;justify-content:center;border-radius:0 0 4px 4px}
.social-tab{left:740px;top:0;width:148px;height:34px;background:var(--black);border-radius:0 0 4px 4px;display:flex;align-items:center;justify-content:center;gap:11px}
.social-tab span{width:23px;height:23px;border-radius:3px;background:#3b7cc4}
.social-tab span:last-child{background:#cfcfcf}
.quote-line{right:117px;top:71px;font-family:"Ubuntu",sans-serif;font-weight:500;font-size:19px;color:var(--blue);display:flex;align-items:center;gap:6px;white-space:nowrap}
.quote-line b{color:var(--ink);font-weight:500}
.quote-line .phone-num{color:var(--ink);margin-left:6px}

/* nav */
.nav{left:0;top:108px;width:1005px;height:37px;background:linear-gradient(#1581b5,#085c86);display:flex;padding-left:117px}
.nav a{font-family:"Ubuntu",sans-serif;font-size:13px;color:#d8e9f3;text-decoration:none;display:flex;align-items:center;justify-content:center;border-right:1px solid #0a557c}
.nav a.active{background:var(--black);color:var(--white)}

/* hero */
.hero{left:0;top:145px;width:1005px;height:375px;background:linear-gradient(180deg,#3d5a3a 0%,#5e7550 30%,#3f4a3a 60%,#2e3630 100%)}
.hero-caption{left:352px;top:252px;width:300px;text-align:center;font-family:"Ubuntu",sans-serif;font-style:italic;font-weight:500;font-size:19.5px;line-height:26px;color:var(--white);text-shadow:0 1px 3px rgba(0,0,0,.6)}
.search-bar{left:0;top:450px;width:1005px;height:29px;background:rgba(20,20,22,.82)}
.search-label{left:139px;top:454px;font-family:"Ubuntu",sans-serif;font-weight:500;font-size:17px;color:var(--white)}
.search-button{left:418px;top:450px;width:215px;height:29px;background:var(--blue);color:var(--white);font-family:"Ubuntu",sans-serif;font-weight:500;font-size:16px;display:flex;align-items:center;justify-content:center;gap:7px}
.slider-dots{left:792px;top:458px;display:flex;gap:6px}
.slider-dots i{width:11px;height:11px;border-radius:50%;background:var(--white)}
.slider-dots i.on{background:var(--blue)}

/* footer base */
.footer{left:0;top:983px;width:1005px;height:174px;background:var(--footer)}

/* content card */
.card{left:121px;top:487px;width:762px;height:517px;background:var(--card);border:1px solid #fff;border-radius:3px;box-shadow:0 0 4px rgba(0,0,0,.15)}
.welcome-icon{left:139px;top:510px;width:22px;height:22px;background:var(--blue);border-radius:2px}
.welcome-title{left:171px;top:510px;font-family:"Ubuntu",sans-serif;font-weight:400;font-size:18px;color:var(--blue)}
.welcome-title b{color:var(--ink);font-weight:700}
.welcome-rule{left:139px;top:541px;width:526px;border-top:1px dotted #777}
.welcome-text{left:139px;top:548px;width:530px;font-size:10.6px;line-height:17.2px;color:#3b3b3f}
.welcome-text p+p{margin-top:8px}

.testimonial-tab{left:697px;top:494px;width:161px;height:26px;background:var(--blue);color:var(--white);font-family:"Ubuntu",sans-serif;font-weight:500;font-size:14px;display:flex;align-items:center;justify-content:center}
.testimonial-box{left:690px;top:520px;width:175px;height:190px;border:1px solid #d5d5dc;border-radius:4px;background:#f2f2f6}
.testimonial-quote{left:704px;top:538px;width:156px;font-family:"Ubuntu",sans-serif;font-style:italic;font-size:11.5px;line-height:17px;color:#4a4a4e;white-space:nowrap}
.testimonial-quote .mark{font-size:34px;color:#c8c8ce;line-height:0;vertical-align:-12px;font-style:normal;font-weight:700}
.testimonial-name{left:704px;top:655px;font-family:"Ubuntu",sans-serif;font-weight:500;font-size:12px;color:var(--ink)}
.view-all{left:704px;top:683px;width:58px;height:18px;background:var(--blue);color:var(--white);font-family:"Ubuntu",sans-serif;font-size:11px;display:flex;align-items:center;justify-content:center;border-radius:2px}

.feature{top:732px;width:172px}
.feature h3{font-family:"Ubuntu",sans-serif;font-weight:500;font-size:18px;color:var(--ink);margin-left:4px;height:26px;white-space:nowrap}
.feature h3 span{color:var(--blue)}
.feature .frame{width:170px;height:102px;background:var(--white);border:1px solid #d0d0d6;padding:3px;box-shadow:0 10px 8px -8px rgba(0,0,0,.35)}
.feature .photo{width:100%;height:100%}
.feature p{margin:17px 0 0 5px;font-size:11px;line-height:13.5px;color:#38383c;white-space:nowrap}
.feature p .wide{letter-spacing:.9px}
.feature .read-more{margin:12px 0 0 85px;width:84px;height:17px;display:flex;border-radius:2px;overflow:hidden}
.read-more span{flex:1;background:var(--blue);color:var(--white);font-family:"Ubuntu",sans-serif;font-size:11px;display:flex;align-items:center;justify-content:center}
.read-more i{width:16px;background:#333;display:flex;align-items:center;justify-content:center}

/* footer content */
.footer-col h4{font-family:"Ubuntu",sans-serif;font-weight:500;font-size:13px;color:var(--white);line-height:15px}
.quick-links{left:138px;top:1018px}
.quick-links ul{list-style:none;margin-top:6px}
.quick-links li{font-size:10.5px;line-height:17.8px;color:var(--footer-text)}
.quick-links li::before{content:"› ";color:#aaa}
.divider{top:1030px;width:1px;height:100px;background:#3a3a3c}
.newsletter{left:288px;top:1018px}
.newsletter small{display:block;margin-top:8px;font-size:9.5px;color:var(--footer-text)}
.newsletter .field{margin-top:8px;width:168px;height:20px;background:var(--white);border:1px solid #999;font-size:9.5px;color:#555;padding:3px 6px}
.newsletter .submit{margin-top:9px;width:78px;height:20px;background:var(--blue);color:var(--white);font-family:"Ubuntu",sans-serif;font-weight:700;font-size:12px;display:flex;align-items:center;justify-content:center}
.contact{left:528px;top:1018px;width:180px}
.contact .row{display:flex;gap:9px;font-size:10px;line-height:14px;color:var(--footer-text);padding:8px 0 9px;border-bottom:1px dotted #555}
.contact .row:last-child{border-bottom:0}
.contact .row svg{flex:none;margin-top:1px}
.footer-brand{left:782px;top:1060px;display:flex;align-items:center;gap:8px;font-family:"Ubuntu",sans-serif;font-weight:700;font-size:13px;line-height:15px;color:#4a5a64}
.footer-brand i{width:22px;height:22px;background:#2b3a44;border-radius:50%}

.bottom-bar{left:0;top:1157px;width:1005px;height:43px;background:var(--blue-band)}
.copyright{left:142px;top:1171px;font-family:"Ubuntu",sans-serif;font-weight:500;font-size:11px;color:var(--white)}
.connected{right:139px;top:1165px;display:flex;align-items:center;gap:10px;font-family:"Ubuntu",sans-serif;font-weight:500;font-size:11px;color:var(--white)}
.connected span{width:23px;height:23px;border-radius:3px;background:#3b7cc4}
.connected span:last-child{background:#cfcfcf}
</style>
</head>
<body>

<header class="abs header"></header>
<div class="abs brand">
  <div class="brand-mark"></div>
  <div class="brand-name">Cedar<br>Reach</div>
</div>
<div class="abs member-tab">Become A Member</div>
<div class="abs social-tab" aria-label="Social links"><span></span><span></span><span></span><span></span></div>
<div class="abs quote-line">Request a <b>FREE</b> Quote
  <svg width="18" height="20" viewBox="0 0 18 20"><path d="M4 1l3 4-2 2c1 3 3 5 6 7l2-2 4 3-2 3C8 18 1 11 1 4z" fill="#222226"/></svg>Call:<span class="phone-num">1.555.204.7716</span>
</div>

<nav class="abs nav">
  <a class="active" style="width:101px">Home</a>
  <a style="width:144px">About Us</a>
  <a style="width:170px">Conversation</a>
  <a style="width:119px">Blog</a>
  <a style="width:130px">Travel</a>
  <a style="width:154px;border-right:0">Contact Us</a>
</nav>

<div class="abs hero" role="img" aria-label="Two anglers kneeling by a forest river, each holding up a large rainbow trout"></div>
<div class="abs hero-caption">Take Your Time And View The Fantastic Fly Fishing And Sport Fishing Destinations.</div>
<div class="abs search-bar"></div>
<div class="abs search-label">WHERE DO YOU WANT TO FISH?</div>
<div class="abs search-button">CHOOSE DESTINATION
  <svg width="13" height="9" viewBox="0 0 13 9"><path d="M1 8l5.5-6L12 8" stroke="#fff" stroke-width="2.6" fill="none"/></svg>
</div>
<div class="abs slider-dots"><i></i><i class="on"></i><i></i><i></i><i></i></div>

<footer class="abs footer"></footer>

<main class="abs card"></main>
<div class="abs welcome-icon"></div>
<h1 class="abs welcome-title">Welcome to <b>Cedar Reach</b></h1>
<div class="abs welcome-rule"></div>
<div class="abs welcome-text">
  <p>Lorem ipsum dolor sit amet, consectetuer adipiscing elit, sed diam nonummy nibh euismod tincidunt ut laoreet dolore magna aliquam erat volutpat. Ut wisi enim ad minim veniam, quis nostrud exerci tation ullamcorper suscipit lobortis nisl ut aliquip ex ea commodo consequat. Duis autem vel eum iriure dolor in hendrerit in vulputate velit esse molestie consequat.</p>
  <p>Lorem ipsum dolor sit amet, consectetuer adipiscing elit, sed diam nonummy nibh euismod tincidunt ut laoreet dolore magna aliquam erat volutpat. Ut wisi enim ad minim veniam, quis nostrud exerci tation ullamcorper suscipit lobortis nisl ut aliquip ex ea commodo consequat. Duis autem vel eum iriure dolor in hendrerit in vulputate velit esse molestie consequat.</p>
</div>

<div class="abs testimonial-tab">Testimonials</div>
<div class="abs testimonial-box"></div>
<div class="abs testimonial-quote"><span class="mark">“</span> Lorem ipsum dolor sit<br>amet consetug e sed diay<br>nibh euismodl tincidunt ut<br>laoreet dolore magam er vol<br>wisi enim ad minim veniam<br>quis nostrud exerci <span class="mark">”</span></div>
<div class="abs testimonial-name">Mr.Callum Redford</div>
<div class="abs view-all">View All</div>

<section class="abs feature" style="left:139px">
  <h3>Travel <span>Blog</span></h3>
  <div class="frame"><div class="photo" role="img" aria-label="Two anglers standing in a river with fly rods" style="background:linear-gradient(#3f6a34,#6d8a5a 60%,#8a9a88)"></div></div>
  <p><span class="wide">Lorem ipsum dolor sit amet</span><br>consectetuer adipiscing elit, sed<br>diam nonummy nibh</p>
  <div class="read-more"><span>Read More</span><i><svg width="8" height="8"><path d="M1 1l3 3-3 3M4 1l3 3-3 3" stroke="#fff" fill="none"/></svg></i></div>
</section>
<section class="abs feature" style="left:323px">
  <h3>Specials <span>&amp; Deals</span></h3>
  <div class="frame"><div class="photo" role="img" aria-label="Angler in a raft on a lake lined with pine trees" style="background:linear-gradient(#4a8fd0,#2f6a3a 45%,#2a6f8a 70%,#1d5c78)"></div></div>
  <p><span class="wide">Lorem ipsum dolor sit amet</span><br>consectetuer adipiscing elit, sed<br>diam nonummy nibh</p>
  <div class="read-more"><span>Read More</span><i><svg width="8" height="8"><path d="M1 1l3 3-3 3M4 1l3 3-3 3" stroke="#fff" fill="none"/></svg></i></div>
</section>
<section class="abs feature" style="left:508px">
  <h3>Hosted <span>&amp; Trips</span></h3>
  <div class="frame"><div class="photo" role="img" aria-label="Anglers casting from a boat on open sea" style="background:linear-gradient(#5aa3e0,#8fc3ea 50%,#2f7fb8 60%,#1f6aa0)"></div></div>
  <p><span class="wide">Lorem ipsum dolor sit amet</span><br>consectetuer adipiscing elit, sed<br>diam nonummy nibh</p>
  <div class="read-more"><span>Read More</span><i><svg width="8" height="8"><path d="M1 1l3 3-3 3M4 1l3 3-3 3" stroke="#fff" fill="none"/></svg></i></div>
</section>
<section class="abs feature" style="left:692px">
  <h3>Couples<span>/Family</span></h3>
  <div class="frame"><div class="photo" role="img" aria-label="Couple on a boat holding up their catch" style="background:linear-gradient(#6aaee6,#9cc8ea 45%,#7a9a7a 70%,#c9c9c2)"></div></div>
  <p><span class="wide">Lorem ipsum dolor sit amet</span><br>consectetuer adipiscing elit, sed<br>diam nonummy nibh</p>
  <div class="read-more"><span>Read More</span><i><svg width="8" height="8"><path d="M1 1l3 3-3 3M4 1l3 3-3 3" stroke="#fff" fill="none"/></svg></i></div>
</section>

<div class="abs footer-col quick-links">
  <h4>Quick Links</h4>
  <ul><li>Home</li><li>About Us</li><li>Conversation</li><li>Blog</li><li>Travel</li><li>Contact Us</li></ul>
</div>
<div class="abs divider" style="left:253px"></div>
<div class="abs footer-col newsletter">
  <h4>Sign Up For Newsletter</h4>
  <small>Sign up to recieive our free newsletters!</small>
  <div class="field">Name</div>
  <div class="field">Email Address</div>
  <div class="submit">SUBMIT</div>
</div>
<div class="abs divider" style="left:493px"></div>
<div class="abs footer-col contact">
  <h4>Contact Information</h4>
  <div class="row"><svg width="12" height="14" viewBox="0 0 12 14"><path d="M6 0a5 5 0 0 1 5 5c0 4-5 9-5 9S1 9 1 5a5 5 0 0 1 5-5z" fill="#1a8cc4"/><circle cx="6" cy="5" r="2" fill="#1e1e20"/></svg><span>Lorem Ipsum is simply dummy and typesetting industry.</span></div>
  <div class="row"><svg width="12" height="12" viewBox="0 0 12 12"><path d="M2 0l2 3-1 1.5c.8 1.8 2 3 3.6 3.7L8 7l3 2-1.5 2.5C5 11 1 7 .5 2.2z" fill="#1a8cc4"/></svg><span>info@cedarreach.com</span></div>
  <div class="row"><svg width="12" height="10" viewBox="0 0 12 10"><rect x=".5" y=".5" width="11" height="8" fill="#1a8cc4"/><path d="M1 1l5 4 5-4" stroke="#1e1e20" fill="none"/></svg><span>1.555.204.7716</span></div>
</div>
<div class="abs divider" style="left:746px"></div>
<div class="abs footer-brand"><i></i>Cedar<br>Reach</div>

<div class="abs bottom-bar"></div>
<div class="abs copyright">© 2014 Cedar Reach All Rights Reserved.</div>
<div class="abs connected">Connected with Us<span></span><span></span><span></span><span></span></div>

</body>
</html>
```